Professional DJ Business Card

Business card for giving out to clubs and venues or interested groups that are in need of a professional DJ. I want something artistic and catchy/alluring, with a minimalist approach that gets just the vital amount of info and leaves the rest for inquiry via contacting me. Ideally I would like one side to have an image of something cool like an eye and my name, then the other side be the contact info, I am definitely feeling a black or dark colored card, but I am open to other designs. I am uploading a picture that I made that reflects a little of what I am *kind of* looking for.

Industry/Entity Type

Business

Contact Information for Business Card

Tomas Velander (Kalvo)
Professional DJ (West Coast)
EDM (Deep/House/Techno), Hip Hop, Latin, Trap.
Cell: 555-274-8391
Email: Kalvoofficial@mailbrook.net
www.tunevault.net/oxfernwaits

```html
<!DOCTYPE html>
<html lang="en">
<head>
<meta charset="utf-8">
<title>Kalvo – Professional DJ Business Card</title>
<link href="https://fonts.googleapis.com/css2?family=Arimo:wght@400;700&family=Tinos:wght@700&display=swap" rel="stylesheet">
<style>
  :root {
    --page-bg: #d9d6d0;
    --card-dark: #151a16;
    --card-mid: #232a24;
    --ink-light: #f2f2f0;
    --ink-soft: #d8dad6;
    --rule: #9ea39e;
    --band-light: #f4f4f4;
    --band-shade: #c9c9c9;
    --band-ink: #2b2b2b;
    --art-tone: #3a423b;
  }
  * { box-sizing: border-box; margin: 0; padding: 0; }
  html, body { width: 1200px; height: 892px; overflow: hidden; }
  body {
    background: var(--page-bg);
    font-family: "Arimo", Arial, sans-serif;
    position: relative;
  }
  .card {
    position: absolute;
    left: 250px;
    width: 700px;
    height: 400px;
    border-radius: 22px;
    overflow: hidden;
    background: radial-gradient(ellipse at 35% 40%, var(--card-mid), var(--card-dark) 75%);
    box-shadow: 0 10px 24px rgba(0,0,0,.25);
  }
  .card--front { top: 36px; }
  .card--back { top: 456px; }

  /* front side */
  .divider { position: absolute; inset: 0; }
  .brand-art {
    position: absolute;
    left: 48px; top: 60px;
    width: 220px; height: 150px;
    border-radius: 50%;
    background: radial-gradient(ellipse, var(--art-tone), transparent 70%);
  }
  .brand-name {
    position: absolute;
    left: 70px; top: 210px;
    font-family: "Arimo", Arial, sans-serif;
    font-weight: 700;
    font-size: 58px;
    color: var(--ink-light);
    letter-spacing: 1px;
  }
  .profile {
    position: absolute;
    left: 350px; top: 40px;
    color: var(--ink-soft);
    font-size: 19px;
    line-height: 26px;
  }
  .profile__name {
    font-family: "Tinos", "Times New Roman", serif;
    font-weight: 700;
    font-size: 27px;
    color: var(--ink-light);
    margin-bottom: 6px;
  }
  .contact {
    position: absolute;
    left: 350px; top: 225px;
    list-style: none;
    color: var(--ink-light);
    font-size: 21px;
  }
  .contact li { display: flex; align-items: center; gap: 12px; height: 34px; }
  .contact svg { width: 18px; height: 18px; flex: none; }
  .url-band {
    position: absolute;
    left: 0; right: 0; bottom: 0;
    height: 64px;
    background: linear-gradient(to bottom, var(--band-light), var(--band-shade));
    display: flex; align-items: center; justify-content: center;
    color: var(--band-ink);
    font-size: 22px;
    letter-spacing: .5px;
  }

  /* back side */
  .back-art {
    position: absolute;
    left: 250px; top: 70px;
    width: 260px; height: 170px;
    border-radius: 50%;
    background: radial-gradient(ellipse, var(--art-tone), transparent 70%);
  }
  .back-name {
    position: absolute;
    left: 0; right: 0; top: 230px;
    text-align: center;
    font-weight: 700;
    font-size: 78px;
    color: var(--ink-light);
    letter-spacing: 2px;
  }
</style>
</head>
<body>

<section class="card card--front" aria-label="Card front">
  <svg class="divider" viewBox="0 0 700 400" aria-hidden="true">
    <line x1="20" y1="55" x2="335" y2="330" stroke="var(--rule)" stroke-width="1.5"/>
  </svg>
  <div class="brand-art" role="img" aria-label="Sketched eye illustration with radiating strokes"></div>
  <div class="brand-name">Kalvo</div>

  <div class="profile">
    <p class="profile__name">Tomas Velander (Kalvo)</p>
    <p>Professional DJ (West Coast)</p>
    <p>EDM (Deep/House/Techno)</p>
    <p>Hip Hop, Latin, Trap.</p>
  </div>

  <ul class="contact">
    <li>
      <svg viewBox="0 0 18 18" aria-hidden="true"><rect width="18" height="18" rx="2" fill="var(--ink-light)"/><path d="M5 4c1 0 1.5 2 1.5 2.5S5.5 7.5 5.8 8.3c.6 1.4 2 2.8 3.9 3.9.8.3 1.3-.8 1.8-.8s2.5.5 2.5 1.5-1 1.6-2 1.6C8 14.5 3.5 10 3.5 6 3.5 5 4 4 5 4z" fill="var(--card-dark)"/></svg>
      555-274-8391
    </li>
    <li>
      <svg viewBox="0 0 18 18" aria-hidden="true"><rect width="18" height="18" rx="2" fill="var(--ink-light)"/><rect x="3.5" y="5" width="11" height="8" fill="none" stroke="var(--card-dark)" stroke-width="1.4"/><path d="M3.5 5l5.5 4.5L14.5 5" fill="none" stroke="var(--card-dark)" stroke-width="1.4"/></svg>
      Kalvoofficial@mailbrook.net
    </li>
  </ul>

  <div class="url-band">www.tunevault.net/oxfernwaits</div>
</section>

<section class="card card--back" aria-label="Card back">
  <div class="back-art" role="img" aria-label="Sketched eye illustration with radiating strokes"></div>
  <div class="back-name">Kalvo</div>
</section>

</body>
</html>
```